I am looking for business cards and letterhead

I want a high-level look for CEO's who want a concierge level leadership consultant and organization development strategist

This needs to go with my brand: simple, elegant, clean. Please improve on this design while using these fonts and colors

Here is my website: CorinneValdez.com

```html
<!DOCTYPE html>
<html lang="en">
<head>
<meta charset="utf-8">
<title>Business Cards – Front and Back</title>
<link rel="stylesheet" href="https://fonts.googleapis.com/css2?family=Tinos:wght@400;700&display=swap">
<style>
  :root {
    --stage: #1c1c1c;
    --navy: #0a1434;
    --blue: #1a63bd;
    --gold: #e6c98a;
    --ink-light: #f1f1f1;
  }
  * { box-sizing: border-box; margin: 0; padding: 0; }
  html, body {
    width: 1200px;
    height: 1059px;
    overflow: hidden;
    background: var(--stage);
  }
  .canvas {
    position: relative;
    width: 1200px;
    height: 1059px;
    font-family: "Tinos", "Times New Roman", serif;
  }
  .card {
    position: absolute;
    background: var(--navy);
    border-radius: 24px;
    overflow: hidden;
  }
  .card--front { left: 254px; top: 99px; width: 694px; height: 396px; }
  .card--back { left: 254px; top: 550px; width: 706px; height: 401px; }

  .brand-mark {
    position: absolute;
    display: flex;
    align-items: center;
    gap: 10px;
    transform: translate(-50%, -50%);
    color: var(--gold);
    font-weight: 700;
    white-space: nowrap;
  }
  .card--front .brand-mark { left: 216px; top: 201px; font-size: 26px; }
  .card--back .brand-mark { left: 353px; top: 200px; font-size: 32px; }
  .brand-mark__dot {
    width: 14px;
    height: 14px;
    border-radius: 50%;
    background: var(--gold);
    flex: none;
  }
  .card--back .brand-mark__dot { width: 16px; height: 16px; }

  .divider {
    position: absolute;
    left: 349px;
    top: 90px;
    width: 2px;
    height: 221px;
    background: linear-gradient(var(--gold), var(--gold) 80%, rgba(230,201,138,0.2));
  }

  .contact {
    position: absolute;
    left: 377px;
    top: 77px;
    color: var(--ink-light);
  }
  .contact__name {
    margin-left: 9px;
    font-size: 26px;
    font-weight: 700;
    color: var(--blue);
    letter-spacing: 0.4px;
    line-height: 1.2;
  }
  .contact__role {
    margin-left: 9px;
    margin-top: 2px;
    font-size: 18px;
  }
  .contact__list {
    list-style: none;
    margin-top: 21px;
    margin-left: 6px;
  }
  .contact__item {
    display: flex;
    align-items: center;
    height: 32px;
    font-size: 18px;
    white-space: nowrap;
  }
  .contact__icon {
    width: 18px;
    height: 18px;
    margin-right: 12px;
    flex: none;
  }
  .contact__address {
    margin-top: 19px;
    font-size: 18px;
    line-height: 26px;
    font-style: normal;
    white-space: nowrap;
  }

  .accent-band {
    position: absolute;
    left: 0;
    bottom: 0;
    width: 694px;
    height: 10px;
  }
</style>
</head>
<body>
<main class="canvas">

  <section class="card card--front" aria-label="Business card front">
    <div class="brand-mark">
      <span class="brand-mark__dot"></span>
      <span class="brand-mark__name">Northgrove</span>
    </div>

    <div class="divider"></div>

    <div class="contact">
      <h1 class="contact__name">Marlowe Bennett</h1>
      <p class="contact__role">Owner</p>
      <ul class="contact__list">
        <li class="contact__item">
          <svg class="contact__icon" viewBox="0 0 24 24" aria-hidden="true">
            <path fill="var(--gold)" d="M6.6 10.8a15.2 15.2 0 0 0 6.6 6.6l2.2-2.2c.3-.3.7-.4 1-.2 1.1.4 2.3.6 3.6.6.6 0 1 .4 1 1V20c0 .6-.4 1-1 1A17 17 0 0 1 3 4c0-.6.4-1 1-1h3.5c.6 0 1 .4 1 1 0 1.3.2 2.5.6 3.6.1.3 0 .7-.2 1z"/>
            <path fill="none" stroke="var(--gold)" stroke-width="1.6" d="M14 3.5a6.5 6.5 0 0 1 6.5 6.5M14 7a3 3 0 0 1 3 3"/>
          </svg>
          <span>(555) 014-2287</span>
        </li>
        <li class="contact__item">
          <svg class="contact__icon" viewBox="0 0 24 24" aria-hidden="true">
            <rect x="2" y="5" width="20" height="14" fill="var(--gold)"/>
            <path d="M2 5l10 8 10-8" fill="none" stroke="var(--navy)" stroke-width="1.8"/>
          </svg>
          <span>info@northgroveadvisory.com</span>
        </li>
        <li class="contact__item">
          <svg class="contact__icon" viewBox="0 0 24 24" aria-hidden="true">
            <circle cx="12" cy="12" r="10" fill="var(--gold)"/>
            <path fill="var(--navy)" d="M7 6c2 0 3 1 3 3s-2 2-2 4-2 1-3 0a8 8 0 0 1 2-7zM14 13c2 0 3 1 3 3s-1 3-3 4c-1-1-1-3 0-4s-1-2 0-3z"/>
          </svg>
          <span>www.northgroveadvisory.com</span>
        </li>
      </ul>
      <address class="contact__address">
        738, Lakeview Terrace West<br>
        90817, Meridian Bay
      </address>
    </div>

    <svg class="accent-band" viewBox="0 0 694 10" preserveAspectRatio="none" aria-hidden="true">
      <polygon points="0,0 334,0 338,10 0,10" fill="var(--blue)"/>
      <polygon points="339,0 694,0 694,10 343,10" fill="var(--gold)"/>
    </svg>
  </section>

  <section class="card card--back" aria-label="Business card back">
    <div class="brand-mark">
      <span class="brand-mark__dot"></span>
      <span class="brand-mark__name">Northgrove</span>
    </div>
  </section>

</main>
</body>
</html>
```